Business card, Stationery and form for Crane Mill
Crane Mill, LLC an Energy Broker
Professional
Desmond Pilkerton
Principal
47 Birchway Lane
Lakewood, NJ 08539
(555) 214-KELP (5357)
dpilkerton@cranemill.com
www.cranemill.com
I will need to be able to change names etc on them for other workers.
Attached you will find a form that we use regularly (see the comment for the file).
I would also need the stationary designed in a way that is easy to use for word processing in MS Word, such as a template or in a word document that I can type on, besides in any way that may be printed.
I am guessing to use the secondary logo for the back but this is not required. An idea that I had but am unsure how it would look is to make that logo larger and then to place the words inside the lower grey area.
I may choose a full color design with pictures besides the more traditional one which I prefer in order to give the sales force a choice.
This is our primary logo
This is our secondary logo
This is a form which we use regularly. We primarily use the excel version here: http://cranemill.com/wp-content/uploads/2012/03/Crane-Mill-LOA-Form-unprotected.xlsx The form gets minor edits from time to time and I would prefer to have it designed as a header and footer or a template.

```html
<!DOCTYPE html>
<html lang="en">
<head>
<meta charset="utf-8">
<title>Crane Mill Stationery</title>
<link rel="stylesheet" href="https://fonts.googleapis.com/css2?family=Roboto:wght@400;700&display=swap">
<style>
  :root{
    --board-dark:#1f2a36;
    --board-mid:#4b5a6a;
    --steel:#3f4f60;
    --steel-light:#8a97a4;
    --paper:#ffffff;
    --paper-grey:#e4e7ea;
    --brand-blue:#1f86c9;
    --brand-navy:#1d3f5e;
    --ink:#4a4f55;
    --label:#c9d1d9;
  }
  *{box-sizing:border-box;margin:0;padding:0}
  html,body{width:1200px;height:439px;overflow:hidden}
  body{font-family:"Roboto",Arial,sans-serif;color:var(--ink)}
  .board{position:relative;width:1200px;height:439px;
    background:radial-gradient(ellipse at 55% 45%,var(--board-mid) 0%,var(--board-dark) 75%);}
  .piece{position:absolute;box-shadow:0 2px 6px rgba(0,0,0,.45);overflow:hidden}
  .label{position:absolute;font-size:7px;color:var(--label);text-align:center}
  .brand{display:flex;align-items:center;gap:3px;position:absolute}
  .brand-dot{border-radius:50%;background:var(--brand-blue);flex:none}
  .brand-name{font-weight:700;color:var(--brand-navy);letter-spacing:.5px;white-space:nowrap}
  .brand--light .brand-name{color:var(--paper)}
  .tiny{font-size:4px;line-height:6px;color:var(--ink)}
  .card{width:104px;height:60px;background:var(--paper)}
  .card--dark{background:linear-gradient(135deg,var(--steel) 0%,var(--brand-navy) 100%)}
  .letterhead{width:296px;height:380px;background:var(--paper)}
  .watermark{position:absolute;border-radius:10px;
    background:linear-gradient(180deg,#eef4f9 0%,#dde8f1 100%)}
  .envelope{width:306px;height:86px;background:var(--paper-grey)}
  .swoosh{position:absolute;inset:0;width:100%;height:100%}
</style>
</head>
<body>
<main class="board">

  <!-- Business card front -->
  <section class="piece card" style="left:8px;top:48px">
    <svg class="swoosh" viewBox="0 0 104 60" preserveAspectRatio="none" aria-hidden="true">
      <path d="M62 0 H104 V60 H56 Q70 30 62 0Z" fill="#5a6978"/>
      <path d="M60 0 Q68 30 54 60" fill="none" stroke="#b8c0c8" stroke-width="1"/>
    </svg>
    <div class="brand" style="left:5px;top:5px">
      <span class="brand-dot" style="width:8px;height:8px"></span>
      <span class="brand-name" style="font-size:6px">CRANE MILL</span>
    </div>
    <div class="tiny" style="position:absolute;left:5px;top:18px">Desmond Pilkerton<br>Principal</div>
    <div class="tiny" style="position:absolute;left:5px;top:32px;font-size:3.5px;line-height:5px">
      (555) 214-KELP (5357)<br>dpilkerton@cranemill.com<br>47 Birchway Lane, Lakewood, NJ 08539<br>www.cranemill.com
    </div>
  </section>
  <p class="label" style="left:8px;top:112px;width:104px">Front Card</p>

  <!-- Business card back 1 -->
  <section class="piece card" style="left:8px;top:130px">
    <div class="brand" style="left:10px;top:22px">
      <span class="brand-dot" style="width:14px;height:14px"></span>
      <span class="brand-name" style="font-size:11px">CRANE MILL</span>
    </div>
    <div style="position:absolute;left:0;right:0;bottom:0;height:9px;background:var(--steel)"></div>
  </section>
  <p class="label" style="left:8px;top:194px;width:104px">Back Card Option 1</p>

  <!-- Business card back 2 -->
  <section class="piece card card--dark" style="left:8px;top:212px">
    <div class="brand brand--light" style="left:18px;top:24px">
      <span class="brand-dot" style="width:12px;height:12px"></span>
      <span class="brand-name" style="font-size:9px">CRANE MILL</span>
    </div>
  </section>
  <p class="label" style="left:8px;top:276px;width:104px">Back Card Option 2</p>

  <!-- Letterhead option 1 -->
  <section class="piece letterhead" style="left:132px;top:22px">
    <svg class="swoosh" viewBox="0 0 296 380" preserveAspectRatio="none" aria-hidden="true">
      <defs>
        <linearGradient id="lh1band" x1="0" x2="1">
          <stop offset="0" stop-color="#9aa5b0"/><stop offset="1" stop-color="#4c5b6a"/>
        </linearGradient>
      </defs>
      <path d="M262 0 H296 V380 H230 Q276 250 248 150 Q236 70 262 0Z" fill="url(#lh1band)"/>
      <path d="M256 0 Q230 70 242 150 Q270 250 222 380" fill="none" stroke="#c7ced5" stroke-width="2"/>
    </svg>
    <div class="brand" style="left:16px;top:14px">
      <span class="brand-dot" style="width:16px;height:16px"></span>
      <span class="brand-name" style="font-size:10px">CRANE MILL, LLC</span>
    </div>
    <div class="tiny" style="position:absolute;left:36px;top:28px;font-size:4px">an Energy Broker</div>
    <div class="watermark" role="img" aria-label="Faint power line tower illustration" style="left:58px;top:210px;width:120px;height:110px"></div>
    <div class="tiny" style="position:absolute;left:16px;top:330px">
      Desmond Pilkerton<br>47 Birchway Lane<br>Lakewood, NJ 08539<br>(555) 214-KELP (5357)<br>dpilkerton@cranemill.com<br>www.cranemill.com
    </div>
  </section>
  <p class="label" style="left:132px;top:414px;width:296px">Letterhead option 1</p>

  <!-- Letterhead option 2 -->
  <section class="piece letterhead" style="left:512px;top:22px">
    <svg class="swoosh" viewBox="0 0 296 380" preserveAspectRatio="none" aria-hidden="true">
      <defs>
        <linearGradient id="lh2band" x1="0" x2="1">
          <stop offset="0" stop-color="#9aa5b0"/><stop offset="1" stop-color="#4c5b6a"/>
        </linearGradient>
      </defs>
      <path d="M236 0 H296 V380 H272 Q246 250 268 160 Q282 80 236 0Z" fill="url(#lh2band)"/>
      <path d="M228 0 Q274 80 260 160 Q240 250 264 380" fill="none" stroke="#c7ced5" stroke-width="2"/>
    </svg>
    <div class="brand" style="left:76px;top:14px">
      <span class="brand-dot" style="width:16px;height:16px"></span>
      <span class="brand-name" style="font-size:10px">CRANE MILL, LLC</span>
    </div>
    <div class="tiny" style="position:absolute;left:96px;top:28px;font-size:4px">an Energy Broker</div>
    <div class="watermark" role="img" aria-label="Faint power line tower illustration" style="left:58px;top:210px;width:120px;height:110px"></div>
    <div class="tiny" style="position:absolute;left:0;width:260px;top:346px;text-align:center">
      47 Birchway Lane, Lakewood, NJ 08539<br>(555) 214-KELP (5357) · dpilkerton@cranemill.com<br>www.cranemill.com
    </div>
  </section>
  <p class="label" style="left:512px;top:414px;width:296px">Letterhead option 2</p>

  <!-- Envelope back, light -->
  <section class="piece envelope" style="left:878px;top:30px">
    <svg class="swoosh" viewBox="0 0 306 86" preserveAspectRatio="none" aria-hidden="true">
      <path d="M0 0 L153 50 L306 0Z" fill="#f4f5f7" stroke="#c3c9cf" stroke-width="1"/>
    </svg>
  </section>

  <!-- Envelope back, dark -->
  <section class="piece envelope" style="left:890px;top:100px;background:linear-gradient(90deg,var(--steel-light),var(--steel))">
    <svg class="swoosh" viewBox="0 0 306 86" preserveAspectRatio="none" aria-hidden="true">
      <path d="M0 0 L153 46 L306 0Z" fill="#e8ebee"/>
    </svg>
    <div class="brand" style="left:140px;top:16px">
      <span class="brand-dot" style="width:12px;height:12px"></span>
    </div>
  </section>

  <!-- Envelope back, light 2 -->
  <section class="piece envelope" style="left:878px;top:190px">
    <svg class="swoosh" viewBox="0 0 306 86" preserveAspectRatio="none" aria-hidden="true">
      <path d="M0 0 L153 40 L306 0Z" fill="#f4f5f7" stroke="#c3c9cf" stroke-width="1"/>
    </svg>
  </section>

  <!-- Envelope front -->
  <section class="piece envelope" style="left:890px;top:282px;background:var(--paper)">
    <svg class="swoosh" viewBox="0 0 306 86" preserveAspectRatio="none" aria-hidden="true">
      <path d="M210 86 Q250 60 306 58 V86Z" fill="#566574"/>
      <path d="M200 86 Q245 54 306 52" fill="none" stroke="#b8c0c8" stroke-width="1.5"/>
    </svg>
    <div class="brand" style="left:10px;top:8px">
      <span class="brand-dot" style="width:12px;height:12px"></span>
      <span class="brand-name" style="font-size:7px">CRANE MILL, LLC</span>
    </div>
    <div class="tiny" style="position:absolute;left:10px;top:24px">47 Birchway Lane<br>Lakewood, NJ 08539</div>
  </section>
  <p class="label" style="left:878px;top:414px;width:318px">Envelope Front &amp; Back</p>

</main>
</body>
</html>
```